Karvelin PowerPoint Templates

We need a cover page and body page templates for a complete Powerpoint presentation. We administer workers' compensation claims in California mostly to public entities. We offer cloud based software to develop and communicate all the data for each claim. Although we are a technology company, we also see ourselves as the human interface working closely with the client and injured workers.
It all starts with our Logo!
We want to loosely relate our Powerpoint design with our Logo. Maybe just in the color! WE DONT WANT TO RECREATE OUR LOGO AS A PROPOSAL . I've posted the logo and a rough proposal page for reference. We designed it using ArtHive and feel the designer met our criteria very well. As I recall the spec for the logo was to use our name and incorporate "modern, professional and personal" into the design. We will use this template to attract new business. We will be approaching a variety of industries and want the template to be designed specifically for our business identity rather than for clients we are pursuing.
I will also post a simple example of a competitor's PowerPoint presentation for reference.
Please feel free to ask any questions you may have.
Thank You!
Harold

```html
<!DOCTYPE html>
<html lang="en">
<head>
<meta charset="UTF-8">
<title>Karvelin — Body Slide</title>
<link rel="stylesheet" href="https://fonts.googleapis.com/css2?family=Roboto+Condensed:wght@300;400&family=Saira+Semi+Condensed:wght@400;500&display=swap">
<style>
  :root {
    --header-blue: #1b5faf;
    --title-blue: #8cc6f6;
    --heading-blue: #1a8ad4;
    --body-grey: #4d4d4f;
    --panel-blue: #84d4fb;
    --footer-grey: #b5b6b8;
    --white: #ffffff;
  }
  * { margin: 0; padding: 0; box-sizing: border-box; }
  html, body { width: 1200px; height: 900px; overflow: hidden; background: var(--white); }
  .slide { position: relative; width: 1200px; height: 900px; background: var(--white); overflow: hidden; }

  .slide-header {
    position: absolute; left: 0; top: 0; width: 1200px; height: 103px;
    background: var(--header-blue);
  }
  .slide-title {
    position: absolute; left: 30px; top: 22px;
    font-family: "Roboto Condensed", sans-serif; font-weight: 300;
    font-size: 46px; color: var(--title-blue); letter-spacing: 0.3px;
  }
  .brand {
    position: absolute; right: 18px; top: 26px; text-align: right; color: var(--white);
    font-family: "Saira Semi Condensed", sans-serif;
  }
  .brand-name { font-size: 40px; font-weight: 500; line-height: 1; letter-spacing: 0.5px; }
  .brand-tagline { font-size: 12px; font-weight: 400; margin-top: 4px; letter-spacing: 0.2px; }

  .content-block { position: absolute; left: 81px; width: 492px; }
  .content-block--first { top: 186px; }
  .content-block--second { top: 502px; }
  .block-heading {
    font-family: "Saira Semi Condensed", sans-serif; font-weight: 500;
    font-size: 32px; color: var(--heading-blue); line-height: 1.2; margin-bottom: 14px;
  }
  .block-text {
    font-family: "Saira Semi Condensed", sans-serif; font-weight: 400;
    font-size: 22px; line-height: 34.5px; color: var(--body-grey); text-align: justify;
  }

  .media-panel { position: absolute; left: 648px; width: 477px; height: 225px; background: var(--panel-blue); }
  .media-panel--first { top: 199px; }
  .media-panel--second { top: 510px; }

  .slide-footer {
    position: absolute; left: 0; top: 853px; width: 1200px; height: 47px;
    background: var(--footer-grey); color: var(--white);
    font-family: "Roboto Condensed", sans-serif; font-weight: 400; font-size: 21px;
    display: flex; justify-content: space-between; align-items: center; padding: 0 12px;
  }
</style>
</head>
<body>
<main class="slide">
  <header class="slide-header">
    <h1 class="slide-title">Project TItle Here</h1>
    <div class="brand">
      <div class="brand-name">Karvelin</div>
      <div class="brand-tagline">Claims Management Solutions</div>
    </div>
  </header>

  <section class="content-block content-block--first">
    <h2 class="block-heading">Lorem ipsum dolor sit ipsum</h2>
    <p class="block-text">Lorem ipsum dolor sit ipsum Lorem ipsum dolor sit ipsum Lorem ipsum dolor sit ipsum Lorem ipsum dolor sit ipsum lorem ipsum dolor sit ipsum Lorem ipsum dolor sit ipsum Lorem ipsum dolor sit ipsum</p>
  </section>
  <div class="media-panel media-panel--first" role="img" aria-label="Image placeholder"></div>

  <section class="content-block content-block--second">
    <h2 class="block-heading">Lorem ipsum dolor sit ipsum</h2>
    <p class="block-text">Lorem ipsum dolor sit ipsum Lorem ipsum dolor sit ipsum Lorem ipsum dolor sit ipsum Lorem ipsum dolor sit ipsum lorem ipsum dolor sit ipsum Lorem ipsum dolor sit ipsum Lorem ipsum dolor sit ipsum</p>
  </section>
  <div class="media-panel media-panel--second" role="img" aria-label="Image placeholder"></div>

  <footer class="slide-footer">
    <span class="copyright">Copyrightext text here</span>
    <span class="page-number">Page : 01</span>
  </footer>
</main>
</body>
</html>
```